Stationery Design Project for Velmoran Tisk

This project is linked to Corporate Identity of VelmoranTisk.

Our company needs a Stationery Design. Please refer to our original project in the link above.

Stationary
Once The Logo, Look & feel with colour palette and Typography has been set, develop a stationary with the following items:
• Business Card
• Letter A4
• A5 Card
Suggest 3 of each.

Industry/Entity Type

Business

Font styles to use
Other font styles liked:
• Calibri, Arial, Myriad, Helvetica Neue, Lucida Grande, Avenir

```html
<!DOCTYPE html>
<html lang="en">
<head>
<meta charset="utf-8">
<title>Velmoran Tisk — Letterhead A4</title>
<link rel="stylesheet" href="https://fonts.googleapis.com/css2?family=Nunito+Sans:wght@300;400;600&display=swap">
<style>
  :root {
    --backdrop: #ececec;
    --paper: #f7f7f6;
    --ink: #3a3a3a;
    --ink-soft: #6b6b6b;
    --accent: #7d6f66;
    --accent-light: #a89a90;
  }
  * { box-sizing: border-box; margin: 0; padding: 0; }
  html, body {
    width: 1200px; height: 795px; overflow: hidden;
    background: var(--backdrop);
    font-family: "Nunito Sans", "Helvetica Neue", Arial, sans-serif;
    color: var(--ink);
  }
  .canvas {
    position: relative; width: 1200px; height: 795px;
    display: flex; align-items: center; justify-content: center;
  }
  .letterhead {
    position: relative;
    width: 532px; height: 752px;
    background: var(--paper);
    box-shadow: 0 2px 10px rgba(0,0,0,0.08);
    overflow: hidden;
  }
  .letterhead__edge {
    position: absolute; top: 0; right: 0; bottom: 0; width: 7px;
    background: linear-gradient(90deg, var(--accent-light), var(--accent));
  }
  .letterhead__tab {
    position: absolute; top: 0; left: 226px;
    width: 38px; height: 7px; background: var(--accent);
  }
  .brand {
    position: absolute; top: 22px; left: 226px;
    display: flex; align-items: center; gap: 6px;
    font-size: 11px; font-weight: 600; letter-spacing: 0.12em;
    text-transform: uppercase; color: var(--accent);
  }
  .brand__square { width: 8px; height: 8px; background: var(--accent); }
  .sender {
    position: absolute; top: 208px; left: 64px;
    font-size: 7px; line-height: 10px; color: var(--ink-soft);
  }
  .sender p + p { margin-top: 8px; }
  .recipient {
    position: absolute; top: 300px; left: 112px; width: 80px;
    text-align: right;
    font-size: 7px; line-height: 10px; color: var(--ink-soft);
  }
  .recipient p + p { margin-top: 8px; }
  .letter {
    position: absolute; top: 270px; left: 226px; width: 258px;
    font-size: 7px; line-height: 10.5px; color: var(--ink);
    font-weight: 300;
  }
  .letter__subject {
    font-size: 9px; font-weight: 400; letter-spacing: 0.06em;
    text-transform: uppercase; margin-bottom: 10px;
  }
  .letter__body p { margin-bottom: 10px; text-align: left; }
  .letter__closing { margin-top: 80px; color: var(--ink-soft); }
  .letter__closing .signature { margin-top: 14px; }
</style>
</head>
<body>
<main class="canvas">
  <article class="letterhead">
    <div class="letterhead__tab"></div>
    <div class="letterhead__edge"></div>

    <header class="brand">
      <span class="brand__square"></span>
      <span class="brand__name">Velmoran Tisk</span>
    </header>

    <address class="sender">
      <p>Address<br>89 Your Place<br>Your City State<br>09002</p>
      <p>T 123 000 1234<br>F 123 000 1234</p>
      <p>E info@yoursite.com<br>W www.yoursite.com</p>
    </address>

    <div class="recipient">
      <p>Jane<br>11.26.2013</p>
      <p>Address<br>89 Your Place<br>Your City State<br>09002</p>
    </div>

    <section class="letter">
      <h1 class="letter__subject">Vel illum dolore eu</h1>
      <div class="letter__body">
        <p>Lorem ipsum dolor sit amet, consetetur sadipscing elitr, sed diam nonumy eirmod tempor invidunt ut labore et dolore magna aliquyam erat, sed diam voluptua. At vero eos et accusam et justo duo dolores et ea rebum. Stet clita kasd gubergren, no sea takimata sanctus est lorem ipsum dolor sit amet.</p>
        <p>Duis autem vel eum iriure dolor in hendrerit in vulputate velit esse molestie consequat, vel illum dolore eu feugiat nulla facilisis at vero eros et accumsan et iusto odio dignissim qui blandit praesent luptatum zzril delenit augue duis dolore te feugait nulla facilisi. Lorem ipsum dolor sit amet.</p>
        <p>Lorem ipsum dolor sit amet, consetetur sadipscing elitr, sed diam nonumy eirmod tempor invidunt ut labore et dolore magna aliquyam erat, sed diam voluptua. At vero eos et accusam et justo duo dolores et ea rebum. Stet clita kasd gubergren, no sea takimata sanctus est lorem ipsum dolor sit amet.</p>
        <p>Lorem ipsum dolor sit amet, consetetur sadipscing elitr, sed diam nonumy eirmod tempor invidunt ut labore et dolore magna aliquyam erat, sed diam voluptua. At vero eos et accusam et justo duo dolores et ea rebum. Stet clita kasd gubergren, no sea takimata sanctus est lorem ipsum dolor sit amet.</p>
      </div>
      <div class="letter__closing">
        <p>Best regards,</p>
        <p class="signature">John Doe<br>President CEO</p>
      </div>
    </section>
  </article>
</main>
</body>
</html>
```